TalkBridge - Language Coaching Services

Sleek, innovative, trendy design for Language Coaching business.

TalkBridge is a new UK based company that provides Language Coaching services. We offer highly personalized on-line and face to face language courses. We also impart learning techniques workshops based on the latest neuroscience research for second-language acquisition.

Target Market(s)

Industry/Entity Type

Consulting

Contact Information for Business Card

TalkBridge
ElenaVT@talkbridge-demo.co.uk
TalkBridge-demo.co.uk
London, UK

Font styles to use
Sans Serif

```html
<!DOCTYPE html>
<html lang="en">
<head>
<meta charset="utf-8">
<title>TalkBridge Business Card</title>
<link href="https://fonts.googleapis.com/css2?family=Lato:wght@300;400;700&display=swap" rel="stylesheet">
<style>
  :root {
    --backdrop: #1e1f21;
    --blue-light: #2aa6c9;
    --blue-mid: #1f8db4;
    --blue-deep: #176f99;
    --brand-blue: #1b7fae;
    --white: #ffffff;
    --paper: #f7f8f9;
  }
  * { margin: 0; padding: 0; box-sizing: border-box; }
  html, body { width: 1200px; height: 900px; overflow: hidden; }
  body {
    background: var(--backdrop);
    font-family: "Lato", sans-serif;
    position: relative;
  }
  .card {
    position: absolute;
    width: 560px;
    height: 320px;
    overflow: hidden;
    box-shadow: 0 14px 30px rgba(0,0,0,0.45);
  }
  /* Front */
  .card-front {
    left: 320px;
    top: 100px;
    background: linear-gradient(210deg, var(--blue-deep) 0%, var(--blue-mid) 50%, var(--blue-light) 100%);
  }
  .front-circle {
    position: absolute;
    left: 200px;
    top: 60px;
    width: 170px;
    height: 170px;
    border-radius: 50%;
    border: 10px solid rgba(255,255,255,0.12);
  }
  .front-name {
    position: absolute;
    left: 0;
    right: 0;
    top: 120px;
    text-align: center;
    color: var(--white);
    font-weight: 400;
    font-size: 50px;
    letter-spacing: 2px;
    text-transform: uppercase;
  }
  .front-web {
    position: absolute;
    left: 0;
    right: 0;
    top: 240px;
    text-align: center;
    color: var(--white);
    font-size: 13px;
    font-weight: 400;
    letter-spacing: 5px;
  }
  /* Back */
  .card-back {
    left: 320px;
    top: 480px;
    background: linear-gradient(210deg, var(--blue-deep) 0%, var(--blue-mid) 55%, var(--blue-light) 100%);
  }
  .back-disc {
    position: absolute;
    left: -280px;
    top: -60px;
    width: 620px;
    height: 620px;
    border-radius: 50%;
    background: var(--paper);
  }
  .back-brand {
    position: absolute;
    left: 34px;
    top: 140px;
    display: flex;
    align-items: center;
    gap: 12px;
  }
  .brand-dot {
    width: 34px;
    height: 34px;
    border-radius: 50%;
    border: 4px solid var(--brand-blue);
  }
  .brand-name {
    color: var(--brand-blue);
    font-weight: 400;
    font-size: 32px;
    letter-spacing: 1px;
    text-transform: uppercase;
  }
  .contact {
    position: absolute;
    left: 362px;
    top: 56px;
    color: var(--white);
  }
  .person-name { font-size: 15px; font-weight: 300; }
  .person-name strong { font-weight: 700; }
  .person-role { font-size: 10px; font-weight: 300; margin-top: 2px; }
  .address { font-size: 12px; font-weight: 700; margin-top: 18px; line-height: 1.35; }
  .lines { list-style: none; margin-top: 16px; }
  .lines li {
    display: flex;
    align-items: center;
    gap: 8px;
    font-size: 12px;
    font-weight: 400;
    margin-bottom: 6px;
  }
  .icon {
    width: 16px;
    height: 16px;
    flex: none;
  }
</style>
</head>
<body>
  <section class="card card-front">
    <div class="front-circle"></div>
    <div class="front-name">TalkBridge</div>
    <div class="front-web">www.TalkBridge-demo.co.uk</div>
  </section>

  <section class="card card-back">
    <div class="back-disc"></div>
    <div class="back-brand">
      <span class="brand-dot"></span>
      <span class="brand-name">TalkBridge</span>
    </div>
    <div class="contact">
      <p class="person-name">Elena <strong>Vance</strong></p>
      <p class="person-role">Chief Executive Officer</p>
      <p class="address">14 Harbour Lane, Suite 5<br>London, UK EC1A 4ZZ</p>
      <ul class="lines">
        <li>
          <svg class="icon" viewBox="0 0 16 16"><circle cx="8" cy="8" r="8" fill="#fff"/><path d="M5 4.5h1.6l.7 2-1 .7a5 5 0 0 0 2.5 2.5l.7-1 2 .7V11a.9.9 0 0 1-1 .9A6.5 6.5 0 0 1 4.1 5.5 .9.9 0 0 1 5 4.5z" fill="#1f8db4"/></svg>
          020.7946.0182
        </li>
        <li>
          <svg class="icon" viewBox="0 0 16 16"><circle cx="8" cy="8" r="8" fill="#fff"/><rect x="4" y="6" width="8" height="5" rx="1" fill="#1f8db4"/><rect x="5.5" y="4" width="5" height="2.5" fill="#1f8db4"/></svg>
          020.7946.0547
        </li>
        <li>
          <svg class="icon" viewBox="0 0 16 16"><circle cx="8" cy="8" r="8" fill="#fff"/><rect x="4" y="5.2" width="8" height="5.6" rx="0.6" fill="#1f8db4"/><path d="M4.3 5.6 8 8.4l3.7-2.8" stroke="#fff" stroke-width="0.9" fill="none"/></svg>
          ElenaVT@talkbridge-demo.co.uk
        </li>
      </ul>
    </div>
  </section>
</body>
</html>
```